Website for Fashion/Jewelry online seller

We would like a website design that can be used in wordpress. It will be important to be able to link instagram, twitter, etc posts on the bottom of site. We are to be a online seller of chic jewelry, art, fashion, and other home design industries. Currently we emphasize jewelry but as the years move forward, other products will be introduced as collections in home furnishings and primarily women's fashion. It will be important to have a “shop now” section where people can order products online so ecommerce will need to be set up at some point. The website should have the following feel: clean, modern, contemporary and chic. A lot of whites should be used with simple text and simple but elegant fonts. Best is to go to mirevantello.com to get the best idea of what we are wanting for the look and feel of the site.

Target Market(s)

upper social class people that are into fashion, jewelry, etc

Industry/Entity Type

Fashion

Number of Pages Required

5+ page

Font styles to use
Other font styles liked:
• go to daskorvin.com to see the font desired

Requirements
Must have
• Name of Company is Tide Hollow 7
Nice to have
• see project description
Should not have
• see project description

```html
<!DOCTYPE html>
<html lang="en">
<head>
<meta charset="utf-8">
<title>Tide Hollow 7 — Lookbook Fashion</title>
<link href="https://fonts.googleapis.com/css2?family=Josefin+Sans:wght@300;400;600&family=Open+Sans:wght@400;600&display=swap" rel="stylesheet">
<style>
  :root{
    --white:#ffffff;
    --ink:#3a3a3a;
    --muted:#8a8a8a;
    --accent:#f26a3d;
    --band:#e9e9e9;
    --footer:#4a4a4a;
    --hero-a:#8c8c8c;
    --hero-b:#5e5e5e;
    --sidebar:rgba(60,60,60,.55);
    --head:'Josefin Sans', sans-serif;
    --body:'Open Sans', sans-serif;
  }
  *{box-sizing:border-box;margin:0;padding:0}
  html,body{width:774px;height:1200px;overflow:hidden;background:var(--white)}
  body{position:relative;font-family:var(--body);color:var(--ink)}
  h1,h2{font-weight:400}
  .abs{position:absolute}

  /* hero */
  .hero{left:0;top:0;width:774px;height:440px;background:linear-gradient(120deg,var(--hero-a),#b3b3b3 45%,var(--hero-b))}
  .hero-photo{left:232px;top:0;width:542px;height:440px;background:radial-gradient(ellipse at 45% 40%,#9a8070 0%,#6d6d6d 45%,transparent 75%)}
  .sidebar{left:0;top:0;width:232px;height:440px;background:var(--sidebar)}
  .brand{left:22px;top:24px;font-family:var(--head);font-weight:300;font-size:20px;letter-spacing:1.5px;color:var(--white);white-space:nowrap}
  .nav{left:22px;top:90px;list-style:none}
  .nav li{display:flex;align-items:center;gap:9px;height:27px;font-size:10.5px;letter-spacing:1px;color:var(--white)}
  .nav svg{width:11px;height:11px}
  .kicker{left:232px;width:542px;top:165px;text-align:center;font-family:var(--head);font-size:13px;letter-spacing:1.5px;color:var(--white)}
  .title{left:305px;width:396px;top:186px;padding:8px 0 4px;border-top:1px solid var(--white);border-bottom:1px solid var(--white);text-align:center;font-family:var(--head);font-weight:300;font-size:28px;line-height:30px;letter-spacing:2.5px;color:var(--white);white-space:nowrap}
  .years{left:232px;width:542px;top:240px;text-align:center;font-family:var(--head);font-size:12px;letter-spacing:1.5px;color:var(--white)}
  .btn{display:inline-block;font-size:9.5px;letter-spacing:.8px;text-align:center;text-transform:uppercase;white-space:nowrap}
  .btn-hero{top:270px;width:98px;height:26px;line-height:26px}
  .btn-shop{left:402px;background:var(--accent);color:var(--white)}
  .btn-learn{left:510px;background:var(--white);color:var(--ink)}
  .dots{left:452px;top:376px;display:flex;gap:5px}
  .dots span{width:6px;height:6px;border-radius:50%;background:var(--white);opacity:.6}
  .dots span:first-child{opacity:1}

  /* new arrival */
  .section-title{left:0;width:774px;top:462px;text-align:center;font-family:var(--head);font-size:14px;letter-spacing:1.5px;color:var(--ink)}
  .section-rule{left:337px;top:484px;width:100px;height:10px}

  .band{left:0;width:774px;background:var(--band)}
  .band-one{top:540px;height:250px}
  .arrow{width:16px;height:22px;background:#6a6a6a;display:flex;align-items:center;justify-content:center}
  .arrow svg{width:8px;height:10px}

  .card{width:156px;background:var(--white);text-align:center}
  .card-img{width:156px;height:162px}
  .card-name{font-size:8.5px;margin-top:10px;color:var(--ink);white-space:nowrap}
  .card-price{font-size:8px;margin-top:3px;color:var(--accent)}
  .btn-card{margin:6px auto 10px;width:54px;height:15px;line-height:15px;font-size:6.5px;background:var(--accent);color:var(--white)}

  .lookbook{left:405px;top:516px;width:369px;height:274px;background:linear-gradient(135deg,#d8d8d8,#9e9e9e 55%,#5d5d5d)}
  .lookbook-frame{left:432px;top:516px;width:216px;height:274px;border:2px solid var(--white);background:rgba(170,150,135,.55)}
  .lookbook-text{left:432px;width:216px;top:618px;text-align:center;font-family:var(--head);font-weight:300;font-size:27px;line-height:31px;letter-spacing:2px;color:var(--white)}

  /* discount + jewelry */
  .band-two{top:842px;height:243px}
  .promo{left:0;top:828px;width:374px;height:262px;background:linear-gradient(135deg,#cfc6bf,#8a7a70 55%,#4e4540)}
  .promo-frame{left:60px;top:850px;width:270px;height:240px;border:2px solid var(--white);background:rgba(110,95,85,.45)}
  .promo-text{left:60px;width:270px;top:925px;text-align:center;font-family:var(--head);font-weight:300;color:var(--white)}
  .promo-text .pct{font-size:48px;line-height:48px}
  .promo-text .word{font-size:36px;line-height:42px}
  .jewel-img{width:144px;height:228px}

  /* footer */
  .footer{left:0;top:1135px;width:774px;height:65px;background:var(--footer);color:var(--white)}
  .footer-copy{left:22px;top:28px;font-size:8px;letter-spacing:.5px}
  .social{left:331px;top:22px;display:flex;gap:10px}
  .social span{width:20px;height:20px;border-radius:50%;background:var(--white);opacity:.9}
  .to-top{left:650px;top:27px;font-size:9px;display:flex;align-items:center;gap:6px}
</style>
</head>
<body>

<header>
  <div class="abs hero"></div>
  <div class="abs hero-photo" role="img" aria-label="Model with long auburn hair seated in dark clothing, hero photograph"></div>
  <nav class="abs sidebar">
    <div class="abs brand">TIDE HOLLOW 7</div>
    <ul class="abs nav">
      <li><svg viewBox="0 0 12 12"><rect x="1" y="3" width="10" height="8" fill="none" stroke="#fff"/><path d="M4 3V1.5h4V3" fill="none" stroke="#fff"/></svg>SHOP</li>
      <li><svg viewBox="0 0 12 12"><circle cx="6" cy="4" r="2.5" fill="#fff"/><path d="M1.5 11.5c0-3 2-4.5 4.5-4.5s4.5 1.5 4.5 4.5z" fill="#fff"/></svg>ABOUT</li>
      <li><svg viewBox="0 0 12 12"><path d="M6 11S1 7.5 1 4.2A2.6 2.6 0 0 1 6 3a2.6 2.6 0 0 1 5 1.2C11 7.5 6 11 6 11z" fill="#fff"/></svg>CHARITY</li>
      <li><svg viewBox="0 0 12 12"><path d="M6 11.5S2 7 2 4.5a4 4 0 0 1 8 0C10 7 6 11.5 6 11.5z" fill="#fff"/><circle cx="6" cy="4.5" r="1.4" fill="#555"/></svg>LOCATIONS</li>
      <li><svg viewBox="0 0 12 12"><path d="M2.5 1h2l1 3-1.3 1a6 6 0 0 0 2.8 2.8l1-1.3 3 1v2c0 .8-.7 1.5-1.5 1.5A9.5 9.5 0 0 1 1 2.5C1 1.7 1.7 1 2.5 1z" fill="#fff"/></svg>CONTACT</li>
    </ul>
  </nav>
  <p class="abs kicker">WHAT TRENDING</p>
  <h1 class="abs title">LOOKBOOK FASHION</h1>
  <p class="abs years">2016-2017</p>
  <span class="abs btn btn-hero btn-shop">Shop now</span>
  <span class="abs btn btn-hero btn-learn">Learn more</span>
  <div class="abs dots"><span></span><span></span><span></span></div>
</header>

<main>
  <h2 class="abs section-title">NEW ARRIVAL</h2>
  <svg class="abs section-rule" viewBox="0 0 100 10"><line x1="0" y1="5" x2="100" y2="5" stroke="#9a9a9a" stroke-width=".8"/><rect x="46" y="1" width="8" height="8" transform="rotate(45 50 5)" fill="#9a9a9a"/></svg>

  <div class="abs band band-one"></div>
  <div class="abs arrow" style="left:46px;top:628px"><svg viewBox="0 0 8 10"><path d="M6 1 2 5l4 4" fill="none" stroke="#fff" stroke-width="1.5"/></svg></div>

  <article class="abs card" style="left:66px;top:544px">
    <div class="card-img" role="img" aria-label="Woman in black hat and long grey cardigan" style="background:linear-gradient(180deg,#efefef,#8d8d8d 55%,#d9d9d9)"></div>
    <p class="card-name">Noir Drape Jacket - Young</p>
    <p class="card-price">$ 48.00</p>
    <span class="btn btn-card">Shop now</span>
  </article>

  <article class="abs card" style="left:232px;top:544px">
    <div class="card-img" role="img" aria-label="Woman in floral sleeveless blouse" style="background:linear-gradient(180deg,#f1f1f1,#b79a8f 50%,#e4e4e4)"></div>
    <p class="card-name">Floral Tie Blouse - Young</p>
    <p class="card-price">$ 36.00</p>
    <span class="btn btn-card">Shop now</span>
  </article>

  <div class="abs arrow" style="left:380px;top:628px"><svg viewBox="0 0 8 10"><path d="M2 1l4 4-4 4" fill="none" stroke="#fff" stroke-width="1.5"/></svg></div>

  <div class="abs lookbook" role="img" aria-label="Black and white fashion portrait of a seated model"></div>
  <div class="abs lookbook-frame"></div>
  <p class="abs lookbook-text">FASHION<br>LOOKBOOK</p>

  <div class="abs band band-two"></div>
  <div class="abs promo" role="img" aria-label="Sepia portrait of a model in a sleeveless top"></div>
  <div class="abs promo-frame"></div>
  <div class="abs promo-text"><div class="pct">50%</div><div class="word">Discount</div></div>

  <div class="abs arrow" style="left:382px;top:936px"><svg viewBox="0 0 8 10"><path d="M6 1 2 5l4 4" fill="none" stroke="#fff" stroke-width="1.5"/></svg></div>

  <article class="abs card" style="left:404px;top:842px;width:144px">
    <div class="jewel-img" role="img" aria-label="Model wearing a statement ring, black and white" style="background:linear-gradient(160deg,#e6e6e6,#8a8a8a 50%,#3d3d3d)"></div>
    <p class="card-name">Fashionable Ring</p>
    <p class="card-price">$ 24.00</p>
    <span class="btn btn-card">Shop now</span>
  </article>

  <article class="abs card" style="left:566px;top:842px;width:156px">
    <div class="jewel-img" role="img" aria-label="Model wearing a fashion necklace, black and white" style="width:156px;background:linear-gradient(200deg,#dedede,#7d7d7d 50%,#353535)"></div>
    <p class="card-name">Fashionable Necklace</p>
    <p class="card-price">$ 32.00</p>
    <span class="btn btn-card">Shop now</span>
  </article>

  <div class="abs arrow" style="left:756px;top:936px"><svg viewBox="0 0 8 10"><path d="M2 1l4 4-4 4" fill="none" stroke="#fff" stroke-width="1.5"/></svg></div>
</main>

<footer class="abs footer">
  <p class="abs footer-copy">TIDE HOLLOW 7 © 2016 Privacy policy</p>
  <div class="abs social"><span></span><span></span><span></span><span></span></div>
  <p class="abs to-top">Back To Top <svg width="9" height="9" viewBox="0 0 10 10"><path d="M1 7l4-4 4 4" fill="none" stroke="#fff" stroke-width="1.5"/></svg></p>
</footer>

</body>
</html>
```